stationary deign for trucking company

im a trucking company looking for a professional set of stationary designs i deliver goods from point a to b
Updates

When submitting stationary designs I need envelope design, letterhead, cards, I’d badge etc

Industry/Entity Type

Trucking Company

Requirements
Must have
• must have letter head, business card, envelope, fax sheet, id badge, folder, thank you card, notebook, invoice sheet.
Nice to have
• nice to have them all custom made (letterhead,envelope, business card, I’d badge etc
Should not have
• must not have prepaid sign want i unique design for items

```html
<!DOCTYPE html>
<html lang="en">
<head>
<meta charset="utf-8">
<title>Harlow Freight + Logistics — Stationery Set</title>
<link rel="stylesheet" href="https://fonts.googleapis.com/css2?family=Montserrat:wght@500;600&family=Open+Sans:wght@400;600&display=swap">
<style>
  :root{
    --bg:#dad8d6;
    --slate:#5e5e60;
    --slate-dark:#4a4a4c;
    --blue:#1f5fb5;
    --band-blue:#d3dfee;
    --band-grey:#e6e6e8;
    --silver-light:#d4d4d7;
    --silver-dark:#9a9a9e;
    --paper:#ffffff;
    --ink:#2b2b2d;
    --muted:#8a8a8d;
  }
  *{box-sizing:border-box;margin:0;padding:0}
  html,body{width:1200px;height:904px;overflow:hidden}
  body{background:var(--bg);font-family:"Open Sans",Arial,sans-serif;position:relative;color:var(--ink)}
  .piece{position:absolute;overflow:hidden}

  /* brand name treatment */
  .brand{display:flex;align-items:center;gap:8px;font-family:"Montserrat",Arial,sans-serif;font-weight:600;position:relative;z-index:1}
  .brand-square{border:2px solid currentColor;flex:none}
  .brand-text{display:flex;flex-direction:column;line-height:1}
  .brand-name{letter-spacing:.12em}
  .brand-tag{letter-spacing:.22em;margin-top:3px}
  .brand--dark{color:var(--ink)}
  .brand--light{color:#fff}

  /* shared footer band for sheets */
  .sheet-band{position:absolute;left:0;bottom:3px;width:100%;background:linear-gradient(180deg,rgba(255,255,255,0) 0%,var(--band-grey) 45%,var(--band-blue) 100%)}
  .sheet-bar{position:absolute;left:0;bottom:0;width:100%;height:3px;background:linear-gradient(90deg,var(--slate-dark) 77%,var(--blue) 77%)}

  /* letterhead */
  .letterhead{left:100px;top:28px;width:345px;height:490px;background:var(--paper)}
  .letterhead .brand{position:absolute;left:22px;top:36px}
  .letterhead .brand-square{width:20px;height:20px}
  .letterhead .brand-name{font-size:15px}
  .letterhead .brand-tag{font-size:4.6px}
  .contact-block{position:absolute;left:230px;top:22px;padding-left:8px;border-left:1px solid #cfcfd2;height:80px;font-size:5.4px;line-height:10px;color:var(--muted)}
  .contact-block .addr{color:var(--blue);font-weight:600}
  .contact-block span.dot{display:inline-block;width:4px;height:4px;border-radius:50%;background:var(--blue);margin-right:3px;vertical-align:middle}
  .letter-body{position:absolute;left:39px;top:110px;width:268px;font-size:6px;line-height:10.7px;color:#7d7d80}
  .letter-body p{margin-bottom:10.7px}
  .signature{position:absolute;left:39px;top:402px;width:110px;height:28px;background:linear-gradient(90deg,#e9e9ec,#f5f5f7);z-index:1}
  .letterhead .sheet-band{height:70px}

  /* folder */
  .folder{left:436px;top:70px;width:344px;height:492px;background:var(--slate)}
  .folder .brand{position:absolute;left:38px;top:220px;gap:16px}
  .folder .brand-square{width:40px;height:40px;border-width:2.5px}
  .folder .brand-name{font-size:30px;font-weight:500;letter-spacing:.14em}
  .folder .brand-tag{font-size:9.5px;font-weight:500;letter-spacing:.28em;margin-top:8px}
  .folder-url{position:absolute;left:0;right:0;top:474px;text-align:center;font-size:7.6px;font-weight:600;color:#fff}
  .folder-bar{position:absolute;left:104px;top:488px;width:140px;height:2px;background:var(--blue)}

  /* business cards */
  .card-back{left:828px;top:84px;width:152px;height:80px;background:var(--slate)}
  .card-back .brand{position:absolute;left:18px;top:28px;gap:6px}
  .card-back .brand-square{width:16px;height:16px;border-width:1.5px}
  .card-back .brand-name{font-size:13px;font-weight:500}
  .card-back .brand-tag{font-size:3.6px}
  .card-front{left:832px;top:206px;width:152px;height:88px;background:var(--paper)}
  .card-front .brand{position:absolute;left:10px;top:38px;gap:4px}
  .card-front .brand-square{width:10px;height:10px;border-width:1.2px}
  .card-front .brand-name{font-size:8px}
  .card-front .brand-tag{font-size:2.6px}
  .card-divider{position:absolute;left:76px;top:16px;width:1px;height:56px;background:#d0d0d3}
  .card-info{position:absolute;left:82px;top:16px;width:66px;font-size:3.6px;line-height:6px;color:var(--muted);white-space:nowrap}
  .card-info .person{font-size:4.6px;font-weight:600;color:var(--blue)}
  .card-info .addr{color:var(--blue);font-weight:600}
  .card-front-bar{position:absolute;left:64px;bottom:0;width:60px;height:2px;background:var(--blue)}

  /* notebook */
  .notebook{left:828px;top:330px;width:148px;height:230px;background:var(--slate);border-radius:0 8px 8px 0}
  .notebook-spine{position:absolute;left:0;top:0;width:6px;height:100%;background:#8c8780}
  .notebook-strap{position:absolute;left:104px;top:0;width:7px;height:100%;background:var(--slate-dark);z-index:2}
  .notebook .brand{position:absolute;left:16px;top:104px;gap:6px}
  .notebook .brand-square{width:18px;height:18px;border-width:1.5px}
  .notebook .brand-name{font-size:13px;font-weight:500}
  .notebook .brand-tag{font-size:4px}
  .notebook-url{position:absolute;left:46px;top:220px;font-size:3.8px;color:#fff}

  /* thank-you card */
  .thanks{left:70px;top:580px;width:340px;height:250px;background:#efefef}
  .thanks-panel{position:absolute;left:0;top:0;width:100%;height:232px;background:linear-gradient(135deg,var(--silver-light) 0%,#e6e6e8 45%,#f2f2f3 100%)}
  .thanks .brand{position:absolute;left:22px;top:26px;gap:7px}
  .thanks .brand-square{width:16px;height:16px;border-width:1.5px}
  .thanks .brand-name{font-size:15px}
  .thanks .brand-tag{font-size:4.2px}
  .thanks-lettering{position:absolute;left:96px;top:106px;width:190px;height:62px;background:linear-gradient(90deg,#c5d2e6,#dbe4f0)}
  .thanks-footer{position:absolute;left:0;bottom:0;width:100%;height:18px;background:var(--ink);color:#fff;font-size:5px;display:flex;align-items:center;justify-content:flex-end;gap:10px;padding-right:12px}

  /* id badge */
  .badge{left:434px;top:650px;width:302px;height:162px;background:var(--slate);border:5px solid #f1f1f1;border-radius:6px}
  .badge-photo{position:absolute;left:12px;top:8px;width:88px;height:92px;background:linear-gradient(180deg,#d7dde4,#9aa4ae);border:2px solid var(--blue)}
  .badge .brand{position:absolute;left:122px;top:20px;gap:10px}
  .badge .brand-square{width:20px;height:20px;border-width:2px}
  .badge .brand-name{font-size:16px;font-weight:500}
  .badge .brand-tag{font-size:4.8px}
  .badge-name{position:absolute;left:150px;top:72px;width:120px;text-align:center;color:#fff;line-height:1.3}
  .badge-name strong{display:block;font-size:11.5px;font-weight:600}
  .badge-name span{font-size:8px}
  .badge-strip{position:absolute;left:0;bottom:0;width:100%;height:40px;background:var(--blue);color:#fff;font-size:9.5px;font-weight:600;display:flex;align-items:flex-end;justify-content:flex-end;padding:0 14px 5px;white-space:nowrap}

  /* envelope */
  .envelope{left:758px;top:676px;width:336px;height:176px;background:var(--paper)}
  .envelope .brand{position:absolute;left:16px;top:18px;gap:6px}
  .envelope .brand-square{width:13px;height:13px;border-width:1.5px}
  .envelope .brand-name{font-size:10.5px}
  .envelope .brand-tag{font-size:3.4px}
  .envelope-addr{position:absolute;left:16px;top:37px;font-size:4px;font-weight:600;color:var(--blue)}
  .envelope .sheet-band{height:60px}
  .envelope .sheet-bar{background:linear-gradient(90deg,var(--slate-dark) 40%,var(--blue) 40%,var(--blue) 72%,var(--slate-dark) 72%)}
</style>
</head>
<body>

<!-- Letterhead -->
<section class="piece letterhead" aria-label="Letterhead">
  <div class="brand brand--dark">
    <span class="brand-square"></span>
    <span class="brand-text"><span class="brand-name">HARLOW</span><span class="brand-tag">FREIGHT + LOGISTICS</span></span>
  </div>
  <div class="contact-block">
    <div class="addr"><span class="dot"></span>Level 00, 00 Harbour Street,<br>&nbsp;&nbsp;Example, 000</div>
    <div><span class="dot"></span>0000 000 000 &nbsp;<span class="dot"></span>0000 000 000</div>
    <div><span class="dot"></span>contact@harlowfreight.com</div>
    <div><span class="dot"></span>www.harlowfreight.com</div>
  </div>
  <div class="letter-body">
    <p>Lorem Ipsum is simply dummy text of the printing and typesetting industry. Lorem Ipsum has been the industry's standard dummy text ever since the 1500s, when an unknown printer took a galley of type and scrambled it to make a type specimen book. It has survived not only five centuries, but also the leap into electronic typesetting, remaining essentially unchanged. It was popularised in the 1960s with the release of Letraset sheets containing Lorem Ipsum passages, and more recently with desktop publishing software including versions of Lorem Ipsum.</p>
    <p>It is a long established fact that a reader will be distracted by the readable content of a page when looking at its layout. The point of using Lorem Ipsum is that it has a more-or-less normal distribution of letters, as opposed to using 'Content here, content here', making it look like readable English. Many desktop publishing packages and web page editors now use Lorem Ipsum as their default model text, and a search for 'lorem ipsum' will uncover many web sites still in their infancy. Various versions have evolved over the years.</p>
    <p>Contrary to popular belief, Lorem Ipsum is not simply random text. It has roots in a piece of classical Latin literature from 45 BC, making it over 2000 years old. A Latin professor looked up one of the more obscure Latin words, consectetur, from a Lorem Ipsum passage, and going through the cites of the word in classical literature, discovered the undoubtable source. Lorem Ipsum comes from sections 1.10.32 and 1.10.33 of "de Finibus Bonorum et Malorum". The generated Lorem Ipsum is therefore always free from repetition, injected humour, or non-characteristic words etc.</p>
  </div>
  <div class="signature" role="img" aria-label="Handwritten signature"></div>
  <div class="sheet-band" role="img" aria-label="Decorative grey and light blue footer wave"></div>
  <div class="sheet-bar"></div>
</section>

<!-- Presentation folder -->
<section class="piece folder" aria-label="Presentation folder">
  <div class="brand brand--light">
    <span class="brand-square"></span>
    <span class="brand-text"><span class="brand-name">HARLOW</span><span class="brand-tag">FREIGHT + LOGISTICS</span></span>
  </div>
  <div class="folder-url">www.harlowfreight.com</div>
  <div class="folder-bar"></div>
</section>

<!-- Business card, back -->
<section class="piece card-back" aria-label="Business card back">
  <div class="brand brand--light">
    <span class="brand-square"></span>
    <span class="brand-text"><span class="brand-name">HARLOW</span><span class="brand-tag">FREIGHT + LOGISTICS</span></span>
  </div>
</section>

<!-- Business card, front -->
<section class="piece card-front" aria-label="Business card front">
  <div class="brand brand--dark">
    <span class="brand-square"></span>
    <span class="brand-text"><span class="brand-name">HARLOW</span><span class="brand-tag">FREIGHT + LOGISTICS</span></span>
  </div>
  <div class="card-divider"></div>
  <div class="card-info">
    <div class="person">Example Name</div>
    <div>Designation</div>
    <div class="addr">Level 00, 00 Harbour St, Example</div>
    <div>0000 000 000 · 0000 000 000</div>
    <div>contact@harlowfreight.com</div>
    <div>www.harlowfreight.com</div>
  </div>
  <div class="card-front-bar"></div>
</section>

<!-- Notebook -->
<section class="piece notebook" aria-label="Notebook cover">
  <div class="notebook-spine"></div>
  <div class="brand brand--light">
    <span class="brand-square"></span>
    <span class="brand-text"><span class="brand-name">HARLOW</span><span class="brand-tag">FREIGHT + LOGISTICS</span></span>
  </div>
  <div class="notebook-strap"></div>
  <div class="notebook-url">www.harlowfreight.com</div>
</section>

<!-- Thank-you card -->
<section class="piece thanks" aria-label="Thank you card">
  <div class="thanks-panel" role="img" aria-label="Decorative silver curved panel"></div>
  <div class="brand brand--dark">
    <span class="brand-square"></span>
    <span class="brand-text"><span class="brand-name">HARLOW</span><span class="brand-tag">FREIGHT + LOGISTICS</span></span>
  </div>
  <div class="thanks-lettering" role="img" aria-label="Hand-lettered thank you script in blue"></div>
  <div class="thanks-footer">
    <span>00 Example Dr, Riverton, EX 00000</span>
    <span>0000-000-000</span>
    <span>contact@harlowfreight.com</span>
    <span>www.harlowfreight.com</span>
  </div>
</section>

<!-- ID badge -->
<section class="piece badge" aria-label="Employee ID badge">
  <div class="badge-photo" role="img" aria-label="Employee portrait photo"></div>
  <div class="brand brand--light">
    <span class="brand-square"></span>
    <span class="brand-text"><span class="brand-name">HARLOW</span><span class="brand-tag">FREIGHT + LOGISTICS</span></span>
  </div>
  <div class="badge-name"><strong>Employee Name</strong><span>Employee Designation</span></div>
  <div class="badge-strip">Card Number&nbsp; 0000000000000000</div>
</section>

<!-- Envelope -->
<section class="piece envelope" aria-label="Envelope">
  <div class="brand brand--dark">
    <span class="brand-square"></span>
    <span class="brand-text"><span class="brand-name">HARLOW</span><span class="brand-tag">FREIGHT + LOGISTICS</span></span>
  </div>
  <div class="envelope-addr">Level 00, 00 Example Street, Example, 2000</div>
  <div class="sheet-band" role="img" aria-label="Decorative grey and light blue footer wave"></div>
  <div class="sheet-bar"></div>
</section>

</body>
</html>
```